An our door sign really promoting our clinic and services

We have a new sports medicine clinic called HALLCREST SPORTS MEDICINE.
We want to make a really nice external sign at our clinic using a photo of our team we really like. I have attached the photo.
We want to simply include our LOGO and also signs with these slogan options. So we want different signs with these different slogans so we can choose what we really like.
This should be a simple and quite design.

The SLOGANS WE WOULD LIKE TO SEE ON THE SIGN (only one slogan per sign in the drafts)

1. Your Journey. Our Expertise
2. Where better health begins
3. Building the best version of you
4. Your health, in expert hands
5. Reaching new heights in your health
6. Your path to peak performance starts here

I have also included different versions of our logo based on the background and how you set the sign up

So summary
1. Image attached
2. Slogan options we would like to see them all
3. Logo attached (various options based on how you set the background up)
4. Size of sign is 2935mm wide x 1885mm high

```html
<!DOCTYPE html>
<html lang="en">
<head>
<meta charset="utf-8">
<title>Hallcrest Sports Medicine – Exterior Sign</title>
<link href="https://fonts.googleapis.com/css2?family=Barlow:ital,wght@0,600;1,800&display=swap" rel="stylesheet">
<style>
  :root {
    --page-bg: #e4e5e7;
    --sign-white: #ffffff;
    --brand-sky: #4bc3ea;
    --brand-navy: #17204a;
    --photo-light: #f3f5f7;
    --photo-mid: #b9c0c6;
    --photo-deep: #56606b;
  }
  html, body {
    margin: 0;
    padding: 0;
    width: 1200px;
    height: 1200px;
    overflow: hidden;
    background: var(--page-bg);
  }
  .sign {
    position: absolute;
    left: 50px;
    top: 247px;
    width: 1100px;
    height: 706px;
    background: var(--sign-white);
  }
  .sign-art {
    display: block;
    width: 100%;
    height: 100%;
  }
  .photo-stop-light { stop-color: var(--photo-light); }
  .photo-stop-mid { stop-color: var(--photo-mid); }
  .photo-stop-deep { stop-color: var(--photo-deep); }
  .rim { fill: var(--brand-navy); }
  .dome { fill: var(--brand-sky); }
  .brand-dot { fill: var(--brand-sky); }
  .brand-name {
    font-family: "Barlow", sans-serif;
    font-weight: 600;
    font-size: 18px;
    letter-spacing: 1.5px;
    fill: var(--brand-navy);
  }
  .slogan {
    font-family: "Barlow", sans-serif;
    font-style: italic;
    font-weight: 800;
    font-size: 54px;
    letter-spacing: -0.5px;
    fill: var(--sign-white);
    text-anchor: middle;
  }
</style>
</head>
<body>
  <div class="sign">
    <svg class="sign-art" viewBox="0 0 822 528" xmlns="http://www.w3.org/2000/svg">
      <defs>
        <linearGradient id="team-photo-tone" x1="0" y1="0" x2="1" y2="0.3">
          <stop offset="0" class="photo-stop-light"/>
          <stop offset="0.35" class="photo-stop-light"/>
          <stop offset="0.7" class="photo-stop-mid"/>
          <stop offset="1" class="photo-stop-deep"/>
        </linearGradient>
        <clipPath id="photo-window">
          <circle cx="410" cy="110" r="440"/>
        </clipPath>
      </defs>

      <g class="team-photo" role="img" aria-label="Photo of two clinic team members reviewing a tablet together in the gym">
        <rect x="0" y="0" width="822" height="528" fill="url(#team-photo-tone)" clip-path="url(#photo-window)"/>
      </g>

      <g class="brand-lockup">
        <circle class="brand-dot" cx="66" cy="78" r="9"/>
        <text class="brand-name" x="84" y="85">HALLCREST SPORTS MEDICINE</text>
      </g>

      <circle class="rim" cx="425" cy="650" r="420"/>
      <circle class="dome" cx="411" cy="655" r="409"/>

      <text class="slogan" x="412" y="404">YOUR JOURNEY.</text>
      <text class="slogan" x="412" y="472">OUR EXPERTISE</text>
    </svg>
  </div>
</body>
</html>
```